Medical equipment business looking for professional, unique business card

We need a business card design for a durable medical equipment company. We are small but would like our cards to express that we are much bigger. We focus on braces (back, knee, wrist, etc) but also do crutches, rollators, wheelchairs- basically medical equipment that gets you going and back in Action. Our colors are blue and green and our logo has an arrow and use of a "spine". We'd like to express professionalism while being unique.

Industry/Entity Type

Medical Equipment

Contact Information for Business Card

Professional feel but unique. Memorable.

Font styles to use
Serif
Sans Serif
Other font styles liked:
• verdana

Requirements
Must have
• card holders cell#, business phone#, fax#, email, website address, business address, logo
Nice to have
• use of medical/healthcare related descriptive words, items, look
Should not have
• the wrong colors or cartoon characters.

```html
<!DOCTYPE html>
<html lang="en">
<head>
<meta charset="utf-8">
<title>Stridewell DME – Business Card</title>
<link rel="stylesheet" href="https://fonts.googleapis.com/css2?family=Open+Sans:wght@400;600;700&display=swap">
<style>
  :root {
    --page-bg: #e7e4df;
    --card-top: #f1f3f4;
    --card-top-shade: #dfe5ea;
    --navy: #1c3550;
    --band-blue: #1d3e5c;
    --band-blue-dark: #15304a;
    --tag-blue: #1f6a9a;
    --green: #5c9a2e;
    --green-light: #7bb342;
    --light-text: #d9d2c6;
    --muted-text: #c9c1b3;
    --divider: #c98a8a;
  }
  * { margin: 0; padding: 0; box-sizing: border-box; }
  html, body {
    width: 1200px; height: 970px; overflow: hidden;
    background: var(--page-bg);
    font-family: "Open Sans", Verdana, sans-serif;
  }
  .card {
    position: absolute; left: 80px; top: 190px;
    width: 1040px; height: 590px;
    background: linear-gradient(180deg, var(--card-top) 0%, var(--card-top-shade) 100%);
    box-shadow: 0 14px 40px rgba(0,0,0,0.22);
    overflow: hidden;
  }
  .brand {
    position: absolute; left: 0; right: 0; top: 88px;
    display: flex; flex-direction: column; align-items: center;
  }
  .brand-name {
    display: flex; align-items: center; gap: 18px;
    font-size: 78px; font-weight: 600; color: var(--navy);
    letter-spacing: -1px; line-height: 1;
  }
  .brand-dot {
    width: 30px; height: 30px; border-radius: 50%;
    background: var(--green);
  }
  .brand-tagline {
    margin-top: 26px; margin-left: 48px;
    font-size: 28px; font-weight: 600; color: var(--tag-blue);
  }
  .info-band {
    position: absolute; left: 0; right: 0; top: 318px; height: 214px;
    background: linear-gradient(180deg, var(--band-blue-dark) 0%, var(--band-blue) 100%);
  }
  .holder {
    position: absolute; right: 550px; top: 30px;
    text-align: right;
  }
  .holder-name {
    font-size: 32px; font-weight: 700; letter-spacing: 1.5px;
    color: var(--light-text); line-height: 1.1;
  }
  .holder-title {
    font-size: 26px; color: var(--green-light); line-height: 1.15;
  }
  .holder-address {
    margin-top: 12px;
    font-size: 26px; color: var(--muted-text); line-height: 1.35;
    letter-spacing: 0.5px;
  }
  .divider {
    position: absolute; left: 519px; top: 38px;
    width: 2px; height: 140px; background: var(--divider);
  }
  .contacts {
    position: absolute; left: 553px; top: 36px;
    list-style: none;
  }
  .contact {
    display: flex; align-items: center; gap: 16px;
    height: 36px;
    font-size: 28px; color: var(--muted-text); letter-spacing: 0.5px;
  }
  .contact-icon {
    width: 28px; height: 26px; flex: none;
  }
  .rule {
    position: absolute; left: 0; right: 0; top: 532px; height: 3px;
    background: #b9c3bf;
  }
  .green-band {
    position: absolute; left: 0; right: 0; top: 535px; bottom: 0;
    background: linear-gradient(90deg, var(--green) 0%, var(--green-light) 50%, var(--green) 100%);
  }
</style>
</head>
<body>
  <div class="card">
    <div class="brand">
      <div class="brand-name"><span class="brand-dot"></span>Stridewell DME</div>
      <div class="brand-tagline">Durable Medical Equipment</div>
    </div>

    <div class="info-band">
      <div class="holder">
        <div class="holder-name">EMPLOYEE NAME</div>
        <div class="holder-title">Managing Director</div>
        <div class="holder-address">PO BOX 123 your address<br>2nd street london ,USA</div>
      </div>

      <div class="divider"></div>

      <ul class="contacts">
        <li class="contact">
          <svg class="contact-icon" viewBox="0 0 28 26" aria-label="Phone">
            <rect width="28" height="26" fill="#5c9a2e"/>
            <path d="M6 10 Q14 3 22 10 L19 12 Q14 9 9 12 Z" fill="#1d3e5c"/>
            <rect x="9" y="13" width="10" height="7" fill="#1d3e5c"/>
          </svg>
          (01) 2345 6789
        </li>
        <li class="contact">
          <svg class="contact-icon" viewBox="0 0 28 26" aria-label="Fax">
            <rect width="28" height="26" fill="#5c9a2e"/>
            <rect x="9" y="4" width="10" height="6" fill="#1d3e5c"/>
            <rect x="5" y="10" width="18" height="9" fill="#1d3e5c"/>
            <rect x="9" y="17" width="10" height="5" fill="#1d3e5c"/>
          </svg>
          (01) 2345 6789
        </li>
        <li class="contact">
          <svg class="contact-icon" viewBox="0 0 28 26" aria-label="Email">
            <rect width="28" height="26" fill="#5c9a2e"/>
            <rect x="5" y="7" width="18" height="12" fill="none" stroke="#1d3e5c" stroke-width="2"/>
            <path d="M5 7 L14 14 L23 7" fill="none" stroke="#1d3e5c" stroke-width="2"/>
          </svg>
          Info@yourcompany.com
        </li>
        <li class="contact">
          <svg class="contact-icon" viewBox="0 0 28 26" aria-label="Website">
            <rect width="28" height="26" fill="#5c9a2e"/>
            <circle cx="14" cy="13" r="8" fill="none" stroke="#1d3e5c" stroke-width="2"/>
            <ellipse cx="14" cy="13" rx="3.5" ry="8" fill="none" stroke="#1d3e5c" stroke-width="1.5"/>
            <line x1="6" y1="13" x2="22" y2="13" stroke="#1d3e5c" stroke-width="1.5"/>
          </svg>
          www.yourcompany.com
        </li>
      </ul>
    </div>

    <div class="rule"></div>
    <div class="green-band"></div>
  </div>
</body>
</html>
```